qTorvix - A forward thinking technology company in the greater Silicon Valley

A .ppt slide deck for a software consulting company. This slide deck will be used for project kick off meetings, sales proposals, and presentations to large audiences that report progress on a variety of projects. It should catch the eye with appealing creativity. Allow for flexibility in space and display. Project well both virtually and in person under varying light conditions. The finished product should give the impression that we are a custom shop but balance in appeal to larger, more traditional companies.

Review of the designs has been delayed due to holiday travel. Thank you for your submissions. I look forward to getting back to you the week of December 3rd.

Target Market(s)

We are an innovative technology company in the greater Silicon Valley. We design and build custom business analytics tools for large, retail corporations. Our solutions deal primarily in the supply chain space but we are leaning towards commercial construction and telecommunications industries. We are targeting prospective clients interested in machine learning and artificial intelligence. Our customers know quality and will pay for a custom solution that exceeds their expectations.

Industry/Entity Type

Business Software

Font styles to use
Sans Serif

Colors

Designer to choose colors to be used in the design.

Requirements
Must have
• Color, graphics, and photos. Multiple different template pages to appeal for graphs, pictures, text, or timelines.
Should not have
• Anything that resembles a "fidget spinner."

```html
<!DOCTYPE html>
<html lang="en">
<head>
<meta charset="utf-8">
<title>qTorvix – Presentation Template</title>
<link href="https://fonts.googleapis.com/css2?family=Nunito:wght@800&family=Open+Sans:wght@400;600;700&display=swap" rel="stylesheet">
<style>
:root{
  --teal:#13a08a;
  --teal-dark:#0b8a83;
  --green:#1ec97a;
  --mint:#3ad3a0;
  --lime:#8cc63f;
  --blue:#2b6f95;
  --ink:#333;
  --muted:#666;
  --grey:#efefef;
  --line:#d8d8d8;
}
*{box-sizing:border-box;margin:0;padding:0}
html,body{width:715px;height:1200px;overflow:hidden;background:#fff}
body{font-family:"Open Sans",Arial,sans-serif;color:var(--ink)}
.deck{display:grid;grid-template-columns:357px 358px;grid-template-rows:repeat(6,200px);width:715px;height:1200px}
.slide{position:relative;overflow:hidden;background:#fff;border:1px solid #e6e6e6}
.abs{position:absolute}
.title{font-family:"Nunito",Arial,sans-serif;font-weight:800;color:var(--teal);text-align:center;font-size:24px;line-height:1}
.lorem{font-size:4.6px;line-height:1.45;color:var(--muted)}
.small{font-size:5.2px;line-height:1.45;color:var(--muted)}
.center{text-align:center}
.photo{background:linear-gradient(135deg,#2c8fa0 0%,#3cb59a 55%,#2a6f93 100%)}

/* cover */
.cover .band{left:0;top:136px;width:100%;height:44px;background:rgba(235,243,245,.92)}
.cover .brand{left:118px;top:141px;display:flex;align-items:center;gap:6px;font-family:"Open Sans",sans-serif;font-weight:600;font-size:21px;color:#44606e;letter-spacing:1px}
.cover .brand i{display:block;width:12px;height:12px;background:var(--green)}
.cover .tag{left:118px;top:167px;font-size:8.4px;color:var(--teal-dark)}

/* icons row */
.disc{width:48px;height:48px;border-radius:50%;background:var(--green);display:flex;align-items:center;justify-content:center}
.disc.dark{background:var(--teal)}
.disc.mint{background:var(--mint)}

/* progress grid */
.box{width:57px;height:34px;color:#fff;font-size:15px;display:flex;align-items:center;justify-content:center}
.c1{background:var(--green)}.c2{background:var(--lime)}.c3{background:var(--mint)}.c4{background:var(--teal)}

/* pricing */
.price{width:98px;height:27px;color:#fff;font-size:8.5px;font-weight:700;display:flex;align-items:center;justify-content:center}
.plist{font-size:5.6px;color:var(--muted);line-height:23px;width:98px}
.plist div{padding-left:20px}

/* products */
.pbox{background:var(--grey);font-size:5.4px;line-height:1.45;padding:8px 4px 4px 10px;color:#333}
.pbox li{margin-left:4px}

/* numbered list */
.num{font-family:"Open Sans",sans-serif;font-size:24px;color:#111;border-right:1px solid #333;padding-right:3px;line-height:1}
.nhead{font-size:5.8px;font-weight:700;letter-spacing:.6px;color:#222}

/* icon circles */
.ring{width:60px;height:60px;border:1.5px solid var(--green);border-radius:50%;display:flex;align-items:center;justify-content:center}
.ihead{font-size:7px;font-weight:700;letter-spacing:.7px;border-bottom:1.5px solid var(--green);padding-bottom:2px;text-align:center;width:74px}

/* team */
.avatar{width:72px;height:72px;border-radius:50%}
.mname{font-size:6.8px;font-weight:700;text-align:center;width:100px}
.mrole{font-size:5.6px;font-style:italic;text-align:center;width:100px;color:#444}

/* contact */
.cl{font-size:5.8px;color:#222;text-align:center;width:110px}
</style>
</head>
<body>
<div class="deck">

  <!-- 1 cover -->
  <section class="slide cover">
    <div class="abs photo" style="inset:0" role="img" aria-label="Photo of a laptop showing an analytics dashboard, tinted teal"></div>
    <div class="abs band"></div>
    <div class="abs brand"><i></i>qTorvix</div>
    <div class="abs tag">Your Partner for Innovative Software Solutions</div>
  </section>

  <!-- 2 about icons -->
  <section class="slide">
    <h2 class="abs title" style="left:0;right:0;top:6px">About Us</h2>
    <p class="abs lorem center" style="left:20px;right:20px;top:37px">Lorem ipsum dolor sit amet, consectetur adipiscing elit, sed do eiusmod tempor incididunt ut labore et dolore magna aliqua. Ut enim ad minim veniam, quis nostrud exercitation ullamco laboris nisi ut aliquip ex ea commodo consequat.</p>
    <div class="abs disc" style="left:31px;top:70px"><svg width="26" height="22"><rect x="2" y="12" width="4" height="9" fill="#f4d03f"/><rect x="8" y="7" width="4" height="14" fill="#e74c3c"/><rect x="14" y="10" width="4" height="11" fill="#3498db"/><rect x="20" y="3" width="4" height="18" fill="#fff"/></svg></div>
    <div class="abs disc dark" style="left:111px;top:70px"><svg width="28" height="20"><rect x="1" y="3" width="26" height="14" rx="2" fill="#fff"/><text x="5" y="14" font-size="10" font-family="Open Sans" fill="#1ec97a" font-weight="700">$</text><rect x="14" y="8" width="10" height="2" fill="#f4d03f"/></svg></div>
    <div class="abs disc mint" style="left:191px;top:70px"><svg width="20" height="26"><rect x="2" y="1" width="16" height="24" fill="#fff"/><circle cx="10" cy="9" r="4.5" fill="#1ec97a"/><rect x="5" y="16" width="10" height="1.5" fill="#aaa"/><rect x="5" y="19" width="10" height="1.5" fill="#aaa"/></svg></div>
    <div class="abs disc mint" style="left:274px;top:70px"><svg width="22" height="26"><circle cx="11" cy="9" r="6" fill="#f4d03f"/><rect x="8" y="15" width="6" height="4" fill="#fff"/><rect x="3" y="20" width="16" height="5" fill="#fff"/></svg></div>
    <p class="abs lorem" style="left:28px;top:130px;width:54px">Lorem ipsum dolor sit amet, consectetur adipiscing elit, sed do eiusmod tempor incididunt ut labore et dolore magna aliqua.</p>
    <p class="abs lorem" style="left:108px;top:130px;width:54px">Lorem ipsum dolor sit amet, consectetur adipiscing elit, sed do eiusmod tempor incididunt ut labore et dolore magna aliqua.</p>
    <p class="abs lorem" style="left:188px;top:130px;width:54px">Lorem ipsum dolor sit amet, consectetur adipiscing elit, sed do eiusmod tempor incididunt ut labore et dolore magna aliqua.</p>
    <p class="abs lorem" style="left:274px;top:130px;width:54px">Lorem ipsum dolor sit amet, consectetur adipiscing elit, sed do eiusmod tempor incididunt ut labore et dolore magna aliqua.</p>
  </section>

  <!-- 3 about quote -->
  <section class="slide">
    <h2 class="abs title" style="left:16px;top:52px;text-align:left">About Us</h2>
    <p class="abs lorem" style="left:16px;top:84px;width:160px;font-size:5.4px">Lorem ipsum dolor sit amet, consectetur adipiscing elit, sed do eiusmod tempor incididunt ut labore et dolore magna aliqua.</p>
    <p class="abs lorem" style="left:16px;top:112px;width:160px;font-size:5.4px">Lorem ipsum dolor sit amet, consectetur adipiscing elit, sed do eiusmod tempor incididunt ut labore et dolore magna aliqua.</p>
    <div class="abs" style="left:193px;top:0;width:164px;height:200px;background:linear-gradient(160deg,#20b98e 0%,#3aa6a8 55%,#7fb3c9 100%)" role="img" aria-label="Photo of a hand pointing at printed charts, tinted green"></div>
    <div class="abs" style="left:193px;width:164px;top:24px;text-align:center;font-family:Nunito,sans-serif;font-weight:800;font-size:34px;color:#fff;line-height:1">&ldquo;</div>
    <p class="abs center" style="left:218px;top:62px;width:114px;font-size:8.4px;line-height:1.4;color:#fff">Lorem ipsum dolor sit amet, consectetur adipiscing elit, sed do eiusmod tempor incididunt ut labore et dolore magna aliqua</p>
  </section>

  <!-- 4 progress grid -->
  <section class="slide">
    <h2 class="abs title" style="left:0;right:0;top:6px">Progress</h2>
    <p class="abs lorem center" style="left:20px;right:20px;top:38px">Lorem ipsum dolor sit amet, consectetur adipiscing elit, sed do eiusmod tempor incididunt ut labore et dolore magna aliqua. Ut enim ad minim veniam, quis nostrud exercitation ullamco laboris nisi ut aliquip ex ea commodo consequat.</p>
    <svg class="abs" style="left:0;top:0" width="357" height="200">
      <g fill="#1ec97a"><rect x="74" y="99" width="4" height="10"/><rect x="74" y="142" width="4" height="10"/><rect x="147" y="99" width="4" height="10"/><rect x="147" y="142" width="4" height="10"/><rect x="230" y="99" width="4" height="10"/><rect x="230" y="142" width="4" height="10"/></g>
      <rect x="205" y="72" width="18" height="4" fill="#8cc63f"/><rect x="120" y="158" width="18" height="4" fill="#3ad3a0"/>
    </svg>
    <div class="abs box c1" style="left:47px;top:66px">[Text]</div>
    <div class="abs box c2" style="left:120px;top:66px">[Text]</div>
    <div class="abs box c3" style="left:203px;top:66px">[Text]</div>
    <div class="abs box c4" style="left:47px;top:109px">[Text]</div>
    <div class="abs box c4" style="left:120px;top:109px">[Text]</div>
    <div class="abs box c2" style="left:203px;top:109px">[Text]</div>
    <div class="abs box c3" style="left:47px;top:152px">[Text]</div>
    <div class="abs box c4" style="left:120px;top:152px">[Text]</div>
    <div class="abs box c1" style="left:203px;top:152px">[Text]</div>
  </section>

  <!-- 5 timeline -->
  <section class="slide">
    <h2 class="abs title" style="left:0;right:0;top:6px">Progress</h2>
    <svg class="abs" style="left:0;top:0" width="357" height="200">
      <g fill="none" stroke-width="2.5">
        <path d="M35 118 H90" stroke="#1ec97a"/>
        <path d="M90 118 H110 V150" stroke="#13a08a"/>
        <path d="M124 118 H160 Q166 118 166 108 V88 Q166 76 180 76 H182 V70" stroke="#1ec97a"/>
        <path d="M196 118 H232 Q238 118 238 128 V160" stroke="#4e9a3a"/>
        <path d="M266 118 H300 Q310 118 310 100 V90 Q310 82 330 82 V70" stroke="#13a08a"/>
        <path d="M182 70 V76" stroke="#1ec97a"/>
      </g>
      <circle cx="182" cy="72" r="3.5" fill="#1ec97a"/><circle cx="102" cy="154" r="3.5" fill="#1ec97a"/>
      <circle cx="248" cy="162" r="3.5" fill="#4e9a3a"/><circle cx="330" cy="70" r="3.5" fill="#13a08a"/>
      <g fill="#fff" stroke="#e2e2e2" stroke-width="1.5">
        <circle cx="35" cy="118" r="14"/><circle cx="107" cy="115" r="14"/><circle cx="181" cy="118" r="14"/><circle cx="253" cy="118" r="14"/><circle cx="330" cy="118" r="14"/>
      </g>
      <g font-family="Open Sans" font-size="8" font-style="italic" font-weight="700" fill="#333" text-anchor="middle">
        <text x="35" y="121">1</text><text x="107" y="118">2</text><text x="181" y="121">3</text><text x="253" y="121">4</text><text x="330" y="121">5</text>
      </g>
    </svg>
    <div class="abs center" style="left:0;top:64px;width:76px;font-size:5px;color:#444"><b style="font-size:6px">Text Title</b><br>This is a sample text, place your own text here</div>
    <div class="abs center" style="left:144px;top:35px;width:76px;font-size:5px;color:#444"><b style="font-size:6px">Text Title</b><br>This is a sample text, place your own text here</div>
    <div class="abs center" style="left:287px;top:35px;width:76px;font-size:5px;color:#444"><b style="font-size:6px">Text Title</b><br>This is a sample text, place your own text here</div>
    <div class="abs center" style="left:64px;top:168px;width:76px;font-size:5px;color:#444"><b style="font-size:6px">Text Title</b><br>This is a sample text, place your own text here</div>
    <div class="abs center" style="left:214px;top:172px;width:76px;font-size:5px;color:#444"><b style="font-size:6px">Text Title</b><br>This is a sample text, place your own text here</div>
  </section>

  <!-- 6 pricing -->
  <section class="slide">
    <h2 class="abs title" style="left:0;right:0;top:8px;font-size:26px">Sales proposals</h2>
    <div class="abs price" style="left:18px;top:60px;background:var(--teal-dark)">$9.90/month</div>
    <div class="abs price" style="left:129px;top:60px;background:var(--mint)">$20/month</div>
    <div class="abs price" style="left:240px;top:60px;background:var(--green)">$50/month</div>
    <div class="abs plist" style="left:18px;top:88px"><div>Lorem ipsum dolor</div><div>Lorem ipsum dolor</div><div>Lorem ipsum dolor</div><div>Lorem ipsum dolor</div></div>
    <div class="abs plist" style="left:129px;top:88px"><div>Lorem ipsum dolor</div><div>Lorem ipsum dolor</div><div>Lorem ipsum dolor</div><div>Lorem ipsum dolor</div></div>
    <div class="abs plist" style="left:240px;top:88px"><div>Lorem ipsum dolor</div><div>Lorem ipsum dolor</div><div>Lorem ipsum dolor</div><div>Lorem ipsum dolor</div></div>
  </section>

  <!-- 7 products -->
  <section class="slide">
    <h2 class="abs title" style="left:0;right:0;top:6px">Products</h2>
    <ul class="abs pbox" style="left:4px;top:38px;width:172px;height:52px"><li>Lorem ipsum dolor sit amet, consectetur adipiscing elitText goes here</li><li>Lorem ipsum dolor sit amet</li></ul>
    <ul class="abs pbox" style="left:180px;top:38px;width:176px;height:52px"><li>Lorem ipsum dolor sit amet, consectetur adipiscing elit, sed do eiusmod tempor incididunt ut labore et dolore magna aliqua.</li><li>Lorem ipsum dolor sit amet</li></ul>
    <svg class="abs" style="left:0;top:96px" width="357" height="34">
      <polygon points="0,0 88,0 98,17 88,34 0,34" fill="#3ad3a0"/>
      <polygon points="90,0 176,0 186,17 176,34 90,34 100,17" fill="#13a08a"/>
      <polygon points="178,0 264,0 274,17 264,34 178,34 188,17" fill="#1ec97a"/>
      <polygon points="266,0 346,0 356,17 346,34 266,34 276,17" fill="#8cc63f"/>
      <g font-family="Open Sans" fill="#fff"><text x="3" y="29" font-size="30">1</text><text x="96" y="29" font-size="30">2</text><text x="184" y="29" font-size="30">3</text><text x="272" y="29" font-size="30">4</text>
      <g font-size="5.4"><text x="25" y="19">Lorem Ipsum</text><text x="120" y="19">Lorem Ipsum</text><text x="208" y="19">Lorem Ipsum</text><text x="296" y="19">Lorem Ipsum</text></g></g>
    </svg>
    <ul class="abs pbox" style="left:4px;top:136px;width:172px;height:58px;padding-top:20px"><li>Lorem ipsum dolor sit ametText goes here</li><li>Lorem ipsum dolor sit amet</li></ul>
    <ul class="abs pbox" style="left:180px;top:136px;width:176px;height:58px"><li>Lorem ipsum dolor sit amet, consectetur adipiscing elit, sed do eiusmod tempor incididunt ut labore et dolore magna aliqua.</li><li>Lorem ipsum dolor sit amet, consectetur adipiscing elit, sed do eiusmod tempor.</li></ul>
  </section>

  <!-- 8 your text photo -->
  <section class="slide">
    <div class="abs" style="left:0;top:0;width:147px;height:200px;background:linear-gradient(160deg,#4aa6a6 0%,#2f9aa0 50%,#5b9fb5 100%)" role="img" aria-label="Photo of a team reviewing charts at a desk, tinted teal"></div>
    <h2 class="abs title" style="left:147px;right:0;top:8px">Your text</h2>
    <p class="abs lorem" style="left:160px;top:70px;width:82px;font-size:5px">Lorem ipsum dolor sit amet, consectetur adipiscing elit, sed do eiusmod tempor incididunt ut labore et dolore magna aliqua Lorem ipsum dolor sit amet, consectetur adipiscing elit, sed do eiusmod tempor incididunt ut labore et dolore magna aliqua</p>
    <p class="abs lorem" style="left:256px;top:60px;width:82px;font-size:5px">Lorem ipsum dolor sit amet, consectetur adipiscing elit, sed do eiusmod tempor incididunt ut labore et dolore magna aliqua Lorem ipsum dolor sit amet, consectetur adipiscing elit, sed do eiusmod tempor incididunt ut labore et dolore magna aliqua Lorem ipsum dolor sit amet, consectetur adipiscing elit, sed do eiusmod tempor incididunt ut labore et dolore magna aliqua</p>
  </section>

  <!-- 9 numbered -->
  <section class="slide" style="border:none">
    <h2 class="abs title" style="left:0;right:0;top:6px">Your text</h2>
    <div class="abs" style="left:10px;top:62px;display:grid;grid-template-columns:repeat(3,111px);row-gap:34px">
      <div style="display:flex;gap:4px"><span class="num">01</span><div><div class="nhead">YOUR TITLE HERE</div><div class="lorem" style="font-size:5.4px">Lorem ipsum dolor sit amet, consectetur adipiscing</div></div></div>
      <div style="display:flex;gap:4px"><span class="num">02</span><div><div class="nhead">YOUR TITLE HERE</div><div class="lorem" style="font-size:5.4px">Lorem ipsum dolor sit amet, consectetur adipiscing</div></div></div>
      <div style="display:flex;gap:4px"><span class="num">03</span><div><div class="nhead">YOUR TITLE HERE</div><div class="lorem" style="font-size:5.4px">Lorem ipsum dolor sit amet, consectetur adipiscing</div></div></div>
      <div style="display:flex;gap:4px"><span class="num">04</span><div><div class="nhead">YOUR TITLE HERE</div><div class="lorem" style="font-size:5.4px">Lorem ipsum dolor sit amet, consectetur adipiscing</div></div></div>
      <div style="display:flex;gap:4px"><span class="num">05</span><div><div class="nhead">YOUR TITLE HERE</div><div class="lorem" style="font-size:5.4px">Lorem ipsum dolor sit amet, consectetur adipiscing</div></div></div>
      <div style="display:flex;gap:4px"><span class="num">06</span><div><div class="nhead">YOUR TITLE HERE</div><div class="lorem" style="font-size:5.4px">Lorem ipsum dolor sit amet, consectetur adipiscing</div></div></div>
    </div>
  </section>

  <!-- 10 icon rings -->
  <section class="slide" style="border:none">
    <h2 class="abs title" style="left:0;right:0;top:6px">Your text</h2>
    <div class="abs ring" style="left:43px;top:60px"><svg width="34" height="28" fill="none" stroke="#222" stroke-width="1.6"><circle cx="11" cy="18" r="5"/><circle cx="11" cy="18" r="8" stroke-dasharray="3 2.3" stroke-width="3"/><circle cx="25" cy="9" r="3.5"/><circle cx="25" cy="9" r="6" stroke-dasharray="2.5 2" stroke-width="2.6"/></svg></div>
    <div class="abs ring" style="left:155px;top:60px"><svg width="30" height="30" fill="none" stroke="#222" stroke-width="1.5"><path d="M10 16 a6 6 0 1 1 10 0 q-2 2-2 5 h-6 q0-3-2-5z"/><path d="M12 24 h6 M13 26.5 h4"/><path d="M15 3 v3 M5 7 l2 2 M25 7 l-2 2 M2 15 h3 M25 15 h3"/></svg></div>
    <div class="abs ring" style="left:272px;top:60px"><svg width="32" height="32" fill="none" stroke="#222" stroke-width="1.5"><circle cx="16" cy="16" r="10"/><circle cx="16" cy="16" r="3"/><path d="M16 2 v8 M16 22 v8 M2 16 h8 M22 16 h8"/></svg></div>
    <div class="abs ihead" style="left:36px;top:128px">Your title here</div>
    <div class="abs ihead" style="left:148px;top:128px">Your title here</div>
    <div class="abs ihead" style="left:265px;top:128px">Your title here</div>
    <p class="abs small center" style="left:32px;top:145px;width:82px">Lorem ipsum dolor sit amet, consectetur adipiscing</p>
    <p class="abs small center" style="left:144px;top:147px;width:82px">Lorem ipsum dolor sit amet, consectetur adipiscing</p>
    <p class="abs small center" style="left:261px;top:145px;width:82px">Lorem ipsum dolor sit amet, consectetur adipiscing</p>
  </section>

  <!-- 11 team -->
  <section class="slide" style="border:none">
    <h2 class="abs title" style="left:0;right:0;top:10px">Our team</h2>
    <div class="abs" style="left:0;right:0;top:65px;height:50px;background:#17c096"></div>
    <div class="abs avatar" style="left:12px;top:54px;background:#e8673c" role="img" aria-label="Portrait of the CEO"></div>
    <div class="abs avatar" style="left:143px;top:53px;background:#dde3ea" role="img" aria-label="Portrait of the Head Manager"></div>
    <div class="abs avatar" style="left:274px;top:53px;background:#e4e4e4" role="img" aria-label="Portrait of the Public Relation lead"></div>
    <div class="abs mname" style="left:-2px;top:134px">INSERT NAME</div>
    <div class="abs mrole" style="left:-2px;top:143px">CEO</div>
    <p class="abs small center" style="left:10px;top:153px;width:76px">Lorem ipsum dolor sit amet, consectetur adipiscing</p>
    <div class="abs mname" style="left:130px;top:133px">INSERT NAME</div>
    <div class="abs mrole" style="left:130px;top:142px">Head Manager</div>
    <p class="abs small center" style="left:142px;top:152px;width:76px">Lorem ipsum dolor sit amet, consectetur adipiscing elit.</p>
    <div class="abs mname" style="left:260px;top:133px">INSERT NAME</div>
    <div class="abs mrole" style="left:260px;top:142px">Public Relation</div>
    <p class="abs small center" style="left:272px;top:152px;width:76px">Lorem ipsum dolor sit amet, consectetur adipiscing elit.</p>
  </section>

  <!-- 12 contact -->
  <section class="slide" style="border:none">
    <div class="abs" style="left:0;right:0;top:2px;height:102px;background:linear-gradient(120deg,#2f8fa6 0%,#2fb39a 60%,#3e8fb2 100%)" role="img" aria-label="Photo of a desk with charts, tinted teal-green"></div>
    <h2 class="abs center" style="left:0;right:0;top:20px;font-family:Nunito,sans-serif;font-weight:800;font-size:20px;color:#fff">Get in touch</h2>
    <p class="abs center" style="left:60px;right:60px;top:46px;font-size:5.6px;line-height:1.4;color:#fff">Lorem ipsum dolor sit amet, consectetur adipiscing elit, sed do eiusmod tempor incididunt ut labore et dolore magna aliqua.</p>
    <svg class="abs" style="left:0;top:0" width="358" height="200" fill="none" stroke="#222" stroke-width="1.4">
      <path d="M40 117 q-3 5 0 10 l2-1 -1-3 q-1-1 0-3 l1-3z" fill="#222"/><path d="M45 119 q2 3 0 6 M48 117 q3 5 0 10"/>
      <rect x="171" y="116" width="14" height="10"/><path d="M171 116 l7 6 7-6 M171 126 l5-5 M185 126 l-5-5"/>
      <circle cx="310" cy="121" r="6" fill="#1da1f2" stroke="none"/>
      <path d="M108 164 q-5-5-5-9 a5 5 0 0 1 10 0 q0 4-5 9z"/><circle cx="108" cy="155" r="1.8"/>
      <circle cx="240" cy="161" r="6"/><ellipse cx="240" cy="161" rx="2.6" ry="6"/><path d="M234 161 h12 M235 158 h10 M235 164 h10"/>
    </svg>
    <div class="abs cl" style="left-0;left:-11px;top:141px">+1 (800) 555-0147</div>
    <div class="abs cl" style="left:123px;top:137px">Your e-mail</div>
    <div class="abs cl" style="left:255px;top:138px">@QTORVIXLABS</div>
    <div class="abs cl" style="left:53px;top:176px;line-height:1.4">Adress, 48 Birch Lane<br>Street, Texas, USA</div>
    <div class="abs cl" style="left:185px;top:183px">https://qtorvixlabs.com/</div>
  </section>

</div>
</body>
</html>
```